Brightwell Recruit Homepage Redesign

Redevelopment work is underway on the Brightwell Recruit website www.brightwell-recruit.com - one task is to create a more compelling vertically stacked, mobile friendly homepage. The developers are not graphic designers and have been unable to produce an effective enough design. Their latest iteration can be seen @ http://dovemark.co.uk/brightwell_recruit/index_5.html

The goal of the current design job is to:

a) produce a homepage design - reworking the attached draft concepts/designs to produce an effective landing page that will entice visitors to respond to the key call to action - to book a meeting with me to discuss their needs
b) ensure the design is aesthetically/functionally aligned with the rest of the site
c) ensure the design supports responsive implementation for viewing on a full range of desktop browsers and mobile devices.

Final output should be in a .psd file with all layers unmerged.

Further details on uploaded docs.

```html
<!DOCTYPE html>
<html lang="en">
<head>
<meta charset="utf-8">
<title>Brightwell Recruit — Leadership Coaching &amp; Assessment</title>
<link rel="stylesheet" href="https://fonts.googleapis.com/css2?family=Montserrat:wght@300;400;500;600&family=Open+Sans:wght@400;600&display=swap">
<style>
:root{
  --white:#ffffff;
  --ink:#3a3f47;
  --muted:#6b7078;
  --navy:#0e2a4a;
  --nav-top:#1f5485;
  --nav-bottom:#0f2f55;
  --sky-top:#4cc3f5;
  --sky-bottom:#1aa2ec;
  --blue-text:#2f8ad8;
  --btn-dark:#12365e;
  --orange:#f28b1e;
  --orange-top:#f6a83b;
  --orange-bottom:#ef7a12;
  --orange-card:#f6a33a;
  --grey-bg:#f1f1f1;
  --card-border:#dcdcdc;
}
*{box-sizing:border-box;margin:0;padding:0}
html,body{width:674px;height:1200px;overflow:hidden}
body{position:relative;background:var(--white);font-family:"Open Sans",Arial,sans-serif;color:var(--ink)}
.abs{position:absolute}
.display{font-family:"Montserrat",Arial,sans-serif;font-weight:300}

/* header */
.site-header{left:0;top:0;width:674px;height:61px;background:var(--white)}
.brand{left:83px;top:14px;display:flex;align-items:center;gap:7px}
.brand-mark{width:22px;height:22px;border-radius:50%;background:var(--orange)}
.brand-name{font-family:"Montserrat",sans-serif;font-weight:600;font-size:14px;color:var(--navy)}
.util-links{right:89px;top:8px;font-size:7.2px;color:var(--muted)}
.util-links span{margin:0 4px}
.social{display:flex;gap:3px}
.social i{display:block;width:14px;height:14px;border-radius:50%;background:var(--orange)}
.header-social{left:516px;top:39px}

.main-nav{left:0;top:61px;width:674px;height:29px;background:linear-gradient(var(--nav-top),var(--nav-bottom));display:flex;justify-content:center;align-items:center;gap:11px;font-family:"Montserrat",sans-serif;font-size:7.2px;color:var(--white)}

/* hero */
.hero{left:0;top:90px;width:674px;height:246px;background:linear-gradient(var(--sky-top),var(--sky-bottom))}
.hero-photo{left:352px;top:10px;width:222px;height:236px;background:linear-gradient(180deg,#5a7fc0,#35579a);border-radius:90px 90px 0 0}
.hero h1{left:79px;top:58px;font-size:19px;color:var(--white);font-weight:300}
.hero h2{left:79px;top:85px;font-size:13px;color:var(--white);font-weight:300}
.hero p{left:81px;top:108px;width:220px;font-size:6.4px;line-height:10px;color:#d9f1fd}
.btn-dark{left:81px;top:137px;width:109px;height:22px;background:var(--btn-dark);border-radius:2px;color:var(--white);font-family:"Montserrat",sans-serif;font-size:7.6px;display:flex;align-items:center;justify-content:center}
.dots{left:83px;top:167px;display:flex;gap:2px}
.dots i{width:7px;height:7px;border-radius:50%;background:#8fd4f7}
.dots i:first-child{background:var(--white)}

/* steps */
.steps-title{left:0;top:362px;width:674px;text-align:center;font-size:18px;color:var(--ink)}
.steps-intro{left:150px;top:389px;width:374px;text-align:center;font-size:6.6px;line-height:11px;color:var(--muted)}
.step-card{top:440px;width:165px;height:182px;border:1px solid var(--card-border);border-radius:2px;background:linear-gradient(#fff 80%,#f3f3f3);text-align:center}
.step-card svg{display:block;margin:11px auto 0}
.step-card h3{font-family:"Montserrat",sans-serif;font-weight:400;font-size:12px;color:var(--blue-text);margin-top:8px}
.step-card .lead{font-size:6.6px;line-height:11px;color:var(--muted);margin-top:4px}
.step-card ul{list-style:none;margin-top:5px;font-size:5.8px;line-height:9.5px;color:var(--muted)}
.step-card li{margin-bottom:6px;padding:0 14px}
.step-card li::before{content:"\2713 ";color:var(--orange);font-weight:600;font-size:8px}

/* audience */
.audience{left:0;top:651px;width:674px;height:245px;background:linear-gradient(var(--orange-top),var(--orange-bottom))}
.audience h2{left:0;top:27px;width:674px;text-align:center;font-size:14px;color:var(--white)}
.aud-card{top:62px;width:160px;height:157px;background:var(--orange-card);text-align:center;color:var(--white)}
.aud-photo{height:74px;background:linear-gradient(135deg,#e7ebef,#9aa3ad)}
.aud-card h3{font-family:"Montserrat",sans-serif;font-weight:400;font-size:11px;line-height:12.5px;margin-top:9px}
.aud-card p{font-size:5.6px;line-height:10.5px;color:#fde3bf;padding:3px 10px 0}

/* video */
.video-section{left:0;top:896px;width:674px;height:212px;background:var(--grey-bg)}
.video-section h2{left:94px;top:47px;font-size:17px;color:var(--ink)}
.video-section h3{left:96px;top:72px;font-family:"Montserrat",sans-serif;font-weight:300;font-size:10px;color:var(--blue-text)}
.video-section p{left:97px;top:90px;width:210px;font-size:6.2px;line-height:11px;color:var(--ink)}
.btn-blue{left:98px;top:118px;width:120px;height:31px;background:linear-gradient(#5a97da,#3a72be);border-radius:2px;color:var(--white);display:flex;align-items:center;gap:9px;padding-left:9px;font-family:"Montserrat",sans-serif;font-size:8.4px;line-height:10px}
.video-frame{left:354px;top:35px;width:213px;height:133px;background:var(--white);border:1px solid #dedede;padding:5px}
.video-still{width:100%;height:100%;background:linear-gradient(135deg,#c58a3a,#8a5a24 50%,#c9dbe8)}
.play{left:96px;top:51px;width:21px;height:21px;border-radius:50%;background:#111;border:1.5px solid #fff}

/* footer */
.site-footer{left:0;top:1108px;width:674px;height:92px;background:var(--navy);text-align:center;color:var(--white)}
.foot-links{margin-top:20px;font-family:"Montserrat",sans-serif;font-size:8px}
.foot-links span{margin:0 3px}
.copyright{margin-top:6px;font-size:5.8px;color:#9fb0c4}
.foot-social{justify-content:center;margin-top:8px}
.foot-social i{width:17px;height:17px;background:var(--white)}
</style>
</head>
<body>

<header class="site-header abs">
  <div class="brand abs"><span class="brand-mark"></span><span class="brand-name">Brightwell Recruit</span></div>
  <div class="util-links abs">Home<span>|</span>About Us<span>|</span>Contact Us</div>
  <div class="social header-social abs"><i></i><i></i><i></i><i></i></div>
</header>

<nav class="main-nav abs">
  <span>Online Leadership Coaching &amp; Assessment</span>
  <span>Transforming Leadership</span>
  <span>Assessments</span>
  <span>Coaching</span>
  <span>Resources &amp; Tools</span>
  <span>Bookings &amp; Prices</span>
</nav>

<section class="hero abs">
  <div class="hero-photo abs" role="img" aria-label="Smiling businessman in a blue shirt with hands pressed together"></div>
  <h1 class="display abs">Want to Motivate Your Team</h1>
  <h2 class="display abs">to Higher Performance Levels?</h2>
  <p class="abs">Etiam est nunc venenatis in tristique eu imperdiet ac nisl Cum sociis natoque penatibus et magnis dis</p>
  <div class="btn-dark abs">Book a Meeting Now</div>
  <div class="dots abs"><i></i><i></i><i></i><i></i></div>
</section>

<h2 class="steps-title display abs">STEPS TO LEADERSHIP SUCCESS</h2>
<p class="steps-intro abs">Etiam est nunc venenatis in tristique eu imperdiet ac nisl Cum sociis natoque penatibus et magnis dis<br>parturient montes nascetur ridiculus mus In iaculis facilisis</p>

<article class="step-card abs" style="left:81px">
  <svg width="46" height="42" viewBox="0 0 46 42" fill="none" stroke="#f28b1e" stroke-width="2">
    <rect x="2" y="5" width="28" height="22"/><line x1="16" y1="1" x2="16" y2="5"/><line x1="10" y1="27" x2="6" y2="38"/><line x1="22" y1="27" x2="26" y2="38"/>
    <g fill="#f28b1e" stroke="none"><rect x="7" y="15" width="3" height="9"/><rect x="12" y="11" width="3" height="13"/><rect x="17" y="17" width="3" height="7"/><circle cx="38" cy="7" r="3.5"/><rect x="34" y="12" width="8" height="28"/></g>
  </svg>
  <h3>Partner &amp; Plan</h3>
  <p class="lead">With an Experienced Leadership<br>Coach to:</p>
  <ul><li>CLARIFY, desired goals and commitment</li><li>ASSESS strengths and development opportunities</li><li>DEFINE leadership coaching plan</li></ul>
</article>

<article class="step-card abs" style="left:254px">
  <svg width="42" height="42" viewBox="0 0 42 42" fill="none" stroke="#f28b1e" stroke-width="1.6">
    <rect x="2" y="2" width="38" height="36"/>
    <path d="M9 9l5 5M14 9l-5 5M20 28l5 5M25 28l-5 5"/><circle cx="11" cy="28" r="3"/>
    <path d="M31 22v8M27 26h8M14 20l14-10M24 10h4v4"/>
  </svg>
  <h3>Work the Plan</h3>
  <p class="lead">With an Experienced Leadership<br>Coach to:</p>
  <ul><li>CLARIFY, desired goals and commitment</li><li>ASSESS strengths and development opportunities</li><li>DEFINE leadership coaching plan</li></ul>
</article>

<article class="step-card abs" style="left:428px">
  <svg width="54" height="42" viewBox="0 0 54 42" fill="#fff" stroke="#f28b1e" stroke-width="2">
    <polyline points="4,20 18,6 32,32 50,12" fill="none"/>
    <circle cx="4" cy="20" r="3"/><circle cx="18" cy="6" r="3"/><circle cx="32" cy="32" r="3"/><circle cx="50" cy="12" r="3"/>
  </svg>
  <h3>Take Stock</h3>
  <p class="lead">With an Experienced Leadership<br>Coach to:</p>
  <ul><li>CLARIFY, desired goals and commitment</li><li>ASSESS strengths and development opportunities</li><li>DEFINE leadership coaching plan</li></ul>
</article>

<section class="audience abs">
  <h2 class="display abs">Who is Leadership Assessment and Coaching for?</h2>
  <article class="aud-card abs" style="left:86px">
    <div class="aud-photo" role="img" aria-label="Leader presenting to colleagues in a meeting room"></div>
    <h3>Organisation Leaders</h3>
    <p>Mauris vel lacus vitae felis vestibulum volutpat Etiam est nunc venenatis in tristique eu imperdiet ac nisl Cum sociis natoque</p>
  </article>
  <article class="aud-card abs" style="left:254px">
    <div class="aud-photo" role="img" aria-label="Managers working together around a table"></div>
    <h3>HR &amp; OD Managers<br>learning officers</h3>
    <p>Mauris vel lacus vitae felis vestibulum volutpat Etiam est nunc venenatis tristique</p>
  </article>
  <article class="aud-card abs" style="left:422px">
    <div class="aud-photo" role="img" aria-label="Group portrait of a business team"></div>
    <h3>Team Leaders</h3>
    <p>Mauris vel lacus vitae felis vestibulum volutpat Etiam est nunc venenatis in tristique eu imperdiet ac nisl Cum sociis natoque</p>
  </article>
</section>

<section class="video-section abs">
  <h2 class="display abs">Watch Our Video</h2>
  <h3 class="abs">Want to know how Brightwell Recruit can help?</h3>
  <p class="abs">Etiam est nunc venenatis in tristique eu imperdiet ac nisl Cum sociis natoque penatibus et magnis dis parturien</p>
  <div class="btn-blue abs">
    <svg width="20" height="18" viewBox="0 0 20 18" fill="#fff"><circle cx="4" cy="3" r="2"/><circle cx="16" cy="3" r="2"/><circle cx="10" cy="2" r="2"/><rect x="2" y="6" width="4" height="8"/><rect x="14" y="6" width="4" height="8"/><rect x="8" y="5" width="4" height="6"/><rect x="6" y="11" width="8" height="2"/><rect x="9" y="13" width="2" height="5"/></svg>
    <span>BOOK A<br>MEETING NOW</span>
  </div>
  <div class="video-frame abs">
    <div class="video-still" role="img" aria-label="Team members stacking their hands together"></div>
    <div class="play abs"><svg width="18" height="18" viewBox="0 0 18 18"><path d="M7 5l6 4-6 4z" fill="#fff"/></svg></div>
  </div>
</section>

<footer class="site-footer abs">
  <div class="foot-links">Home<span>|</span>Transforming Leadership<span>|</span>Assessments<span>|</span>Coaching<span>|</span>Resources &amp; Tools<span>|</span>Booking &amp; Prices</div>
  <div class="copyright">© 2014 Company Name  All right reserved  Term of Use</div>
  <div class="social foot-social"><i></i><i></i><i></i><i></i></div>
</footer>

</body>
</html>
```